Larkhaven Meditation

Logo picture and I want it to say

yoga. meditation. sound healing

small sweet classes

Larkhaven-meditation.example

2417 West Orindale Ave Suite K
Willowmere Bay ca 94620

```html
<!DOCTYPE html>
<html lang="en">
<head>
<meta charset="utf-8">
<title>Larkhaven Meditation – Small Sweet Classes</title>
<link rel="stylesheet" href="https://fonts.googleapis.com/css2?family=Bebas+Neue&family=Montserrat:wght@300;600;700&display=swap">
<style>
  :root {
    --green: #578d6c;
    --green-soft: rgba(80, 138, 102, 0.93);
    --purple: #a98bcc;
    --purple-soft: rgba(160, 125, 200, 0.85);
    --ink: #2a2a2a;
    --paper: #fbfafc;
    --sky-top: #6e9cc4;
    --sky-mid: #b9cfdf;
    --forest: #4e6f5a;
  }
  * { margin: 0; padding: 0; box-sizing: border-box; }
  html, body { width: 900px; height: 1200px; overflow: hidden; background: #ffffff; }
  .flyer {
    position: relative; width: 900px; height: 1200px; overflow: hidden;
    background: var(--paper);
    font-family: "Montserrat", Arial, sans-serif; color: var(--ink);
  }
  .shapes { position: absolute; inset: 0; }
  .brand-mark {
    position: absolute; left: 669px; top: 38px; width: 176px; height: 176px;
    border: 2px solid #3a3a3a; border-radius: 50%; background: #fff;
    display: flex; align-items: center; justify-content: center; text-align: center;
    font-weight: 600; font-size: 19px; line-height: 1.2; color: #3a3a3a;
  }
  .title {
    position: absolute; left: 380px; top: 400px; width: 460px; text-align: center; color: #fff;
    font-weight: normal;
  }
  .title-main { font-family: "Bebas Neue", Impact, sans-serif; font-size: 118px; line-height: 0.9; letter-spacing: 1px; }
  .title-sub { font-weight: 300; font-size: 50px; letter-spacing: 3px; line-height: 1; margin-top: 4px; padding-left: 40px; }
  .tagline {
    position: absolute; left: 0; width: 900px; top: 795px; text-align: center; font-weight: normal;
    font-family: "Bebas Neue", Impact, sans-serif; font-size: 82px; line-height: 1; color: var(--green);
  }
  .tagline .accent { color: var(--purple); }
  .tagline-rule { position: absolute; left: 256px; top: 885px; width: 410px; height: 2px; background: var(--ink); }
  .offer { position: absolute; top: 1025px; font-weight: 600; font-size: 24px; text-align: center; width: 220px; }
  .divider { position: absolute; top: 940px; height: 108px; border-left: 2px dashed #777; }
  .contact { position: absolute; top: 1122px; font-weight: 700; font-size: 17px; line-height: 1.1; white-space: nowrap; }
  .contact-sep { position: absolute; left: 470px; top: 1120px; width: 2px; height: 32px; background: var(--ink); }
</style>
</head>
<body>
<main class="flyer">
  <svg class="shapes" width="900" height="1200" viewBox="0 0 900 1200">
    <defs>
      <linearGradient id="photo-tones" x1="0" y1="0" x2="0" y2="1">
        <stop offset="0" stop-color="var(--sky-top)"/>
        <stop offset="0.45" stop-color="var(--sky-mid)"/>
        <stop offset="0.75" stop-color="var(--forest)"/>
        <stop offset="1" stop-color="#8c8276"/>
      </linearGradient>
      <clipPath id="photo-clip"><circle cx="240" cy="330" r="420"/></clipPath>
    </defs>
    <circle class="photo-ring" cx="258" cy="346" r="424" fill="none" stroke="var(--purple)" stroke-width="10"/>
    <rect class="photo" x="0" y="0" width="900" height="800" fill="url(#photo-tones)" clip-path="url(#photo-clip)"
          role="img" aria-label="Photo of a woman seen from behind in a seated yoga pose, arms raised, above clouds and forested hills"/>
    <circle class="title-disc" cx="655" cy="468" r="258" fill="var(--green-soft)"/>
    <circle class="accent-disc" cx="810" cy="706" r="100" fill="var(--purple-soft)"/>
    <circle class="accent-disc" cx="72" cy="757" r="135" fill="var(--purple-soft)"/>

    <g class="offer-icons">
      <g transform="translate(150 969)">
        <circle cx="-4" cy="3" r="44" fill="var(--purple)"/>
        <circle r="42" fill="var(--green)" stroke="#fff" stroke-width="3"/>
        <circle cy="-14" r="6" fill="#fff"/>
        <path d="M-14 16 Q0 -6 14 16 Z" fill="#fff"/>
      </g>
      <g transform="translate(409 969)">
        <circle cx="-4" cy="3" r="44" fill="var(--purple)"/>
        <circle r="42" fill="var(--green)" stroke="#fff" stroke-width="3"/>
        <path d="M0 -16 Q10 0 0 12 Q-10 0 0 -16 Z M-4 12 Q-20 6 -20 -6 Q-8 -2 -4 12 Z M4 12 Q20 6 20 -6 Q8 -2 4 12 Z" fill="#fff"/>
      </g>
      <g transform="translate(709 969)">
        <circle cx="-4" cy="3" r="44" fill="var(--purple)"/>
        <circle r="42" fill="var(--green)" stroke="#fff" stroke-width="3"/>
        <path d="M-14 14 Q-16 -14 16 -16 Q14 14 -14 14 Z" fill="#fff"/>
        <path d="M-14 14 L6 -6" stroke="var(--green)" stroke-width="2.5"/>
      </g>
    </g>

    <g class="contact-icons">
      <path d="M85 1150 C74 1138 72 1132 72 1126 A13 13 0 0 1 98 1126 C98 1132 96 1138 85 1150 Z" fill="var(--green)"/>
      <circle cx="85" cy="1126" r="5" fill="#fff"/>
      <g transform="translate(548 1137)" fill="none" stroke="var(--green)" stroke-width="2.2">
        <circle r="13"/>
        <ellipse rx="6" ry="13"/>
        <path d="M-13 0 H13 M-11 -6 H11 M-11 6 H11"/>
      </g>
    </g>
  </svg>

  <div class="brand-mark">Larkhaven<br>Meditation</div>

  <h1 class="title">
    <div class="title-main">LARKHAVEN</div>
    <div class="title-sub">MEDITATION</div>
  </h1>

  <h2 class="tagline">SMALL SWEET <span class="accent">CLASSES</span></h2>
  <div class="tagline-rule"></div>

  <div class="offer" style="left:40px">Yoga</div>
  <div class="divider" style="left:267px"></div>
  <div class="offer" style="left:299px">Meditation</div>
  <div class="divider" style="left:553px"></div>
  <div class="offer" style="left:599px">Sound healing</div>

  <div class="contact" style="left:118px">2417 West Orindale Ave Suite K<br>Willowmere Bay ca 94620</div>
  <div class="contact-sep"></div>
  <div class="contact" style="left:577px; top:1128px">Larkhaven-meditation.example</div>
</main>
</body>
</html>
```